Zarvo! Next Steps?, Bail Bond Company Check-in App , Court date, Court Reminders, Payments

Zarvo!
Next Steps?
WINNER OF THIS CONTEST WILL HAVE OPPORTUNITY TO DESIGN CUSTOMIZE SOME OUR COMPANY PAGES AFTER CONTEST!
Check-in with your Bail agent via pic/video
Receive Court reminders
Make a payments

Basically this app is a portal to 3rd party bail companies.
The idea is for the person whom makes bail downloads the Zarvo app from App Store.
Then they select a bail bond company.
This would be similar to a restaurant, real estate agent, insurance agent,,app where we could populate bail bond companies by client location or by typing in name of bail company.
We would like the ability to customize each bail bond company landing pages but are open to a global concept. when you click the bail bond company location it would have the logos for that company so the bail bond company screens would need to be customizeble
The app will require a photo or video check-in that is date and time
stamped with a gps location stored in check-in history
Check-in can be scheduled or random or voluntary
Voluntary and Scheduled Check-ins would require check-in button
Random would be via alert or text

The app should be able to receive court date updates
The app should allow clients to make payments to bail bond company
we need
ZARVO! landing page
client registration screens, check-in screens, available bail bond company screens for client to choose from
client registration page should include
name
email address
phone number
picture
home address
work address
date of birth
this app is different from our u-trak app. this is a bail bond check-in app for third party bail bond companies.
landing page should be ZARVO! Next Steps?
ZARVO ! Registration
Find your bail bond Company should list bail bond companies near me and search bar for searching bail bond companies by name
Next landing pages would be customizable for the third party bail bond companies
these would include pages for
check-ins via pics/videos
payment page
court reminders
contact information for bail bond companies
Zarvo Pages include
initial landing page
registration page
search bail companies

Bail bond company pages should include
Bali bond company landing page
Use KELNOR BAIL BOND COMPANY as example
contact information for bail company
check-in page
payment page
court reminder page
Updates

Low designer entries

Low designer entries

Sick

Sick

Sick

Target Market(s)

Court Defendants, Probation ,jails, sheriffs, judges, attorneys

Industry/Entity Type

justice, law enforcement, courts,

Requirements
Must have
• Check-in via pic/video, ability to receive court date reminders, make paymentswe need client registration screens, check-in screens, available bail bond company screens for client to choose from
Nice to have
• Professional easy to navigate intuitive customizable to 3rd party bail bond companies, logos,phone numbers etc.
Should not have
• unprofessional graphics,

```html
<!DOCTYPE html>
<html lang="en">
<head>
<meta charset="utf-8">
<title>Zarvo – Check-in App Screens</title>
<link rel="stylesheet" href="https://fonts.googleapis.com/css2?family=Poppins:wght@400;500&family=Open+Sans:wght@400;600&display=swap">
<style>
  :root {
    --canvas: #e3e0dc;
    --screen-top: #ececec;
    --surface: #ffffff;
    --surface-soft: #f4f4f5;
    --ink: #2f2f2f;
    --ink-soft: #6f6f6f;
    --field-border: #e3e3e3;
    --brand-blue: #1a87f5;
    --brand-blue-light: #5aaefc;
    --link-blue: #1a7ff0;
    --camera-bar: #333333;
    --shutter: #6b6b6b;
  }
  * { box-sizing: border-box; margin: 0; padding: 0; }
  html, body { width: 1200px; height: 775px; overflow: hidden; }
  body {
    background: var(--canvas);
    font-family: "Open Sans", Arial, sans-serif;
    position: relative;
  }
  .screen {
    position: absolute;
    top: 116px;
    width: 252px;
    height: 547px;
    border-radius: 26px;
    overflow: hidden;
  }

  /* Register screen */
  .register-screen { left: 135px; background: linear-gradient(160deg, var(--screen-top), #f6f6f6 60%, #e4e4e4); }
  .app-title {
    position: absolute; left: 17px; top: 60px;
    font-family: "Poppins", Arial, sans-serif; font-weight: 500;
    font-size: 23px; color: var(--ink);
  }
  .register-card {
    position: absolute; left: 0; top: 113px; width: 100%; bottom: 0;
    background: var(--surface); border-radius: 18px 18px 0 0;
  }
  .card-heading {
    position: absolute; left: 16px; top: 22px;
    font-family: "Poppins", Arial, sans-serif; font-size: 12.5px; color: var(--ink);
  }
  .field {
    position: absolute; left: 15px; width: 222px; height: 35px;
    border: 1px solid var(--field-border); border-radius: 4px;
    background: var(--surface);
    box-shadow: 0 1px 3px rgba(0,0,0,0.06);
    font-size: 10px; color: var(--ink-soft);
    padding-left: 17px; line-height: 33px;
  }
  .field .eye { position: absolute; right: 11px; top: 11px; }
  .primary-button {
    position: absolute; left: 15px; width: 222px;
    background: var(--brand-blue); color: #fff; border-radius: 4px;
    font-weight: 600; text-align: center;
  }
  .register-button { top: 290px; height: 34px; line-height: 34px; font-size: 11px; }
  .divider { position: absolute; left: 15px; width: 222px; top: 352px; height: 1px; background: #e6e6e6; }
  .legal {
    position: absolute; left: 6px; right: 6px; top: 374px;
    font-family: "Poppins", Arial, sans-serif; font-size: 9.5px; line-height: 16px;
    color: var(--ink-soft); text-align: center;
  }
  .legal b { color: var(--link-blue); font-weight: 500; }

  /* Camera check-in screen */
  .camera-screen { left: 489px; background: var(--camera-bar); }
  .photo-area {
    position: absolute; left: 0; top: 0; width: 100%; height: 400px;
    background: linear-gradient(180deg, #7d8794 0%, #9a8571 35%, #7a6248 60%, #4f4a3a 100%);
  }
  .top-bar {
    position: absolute; left: 0; right: 0; top: 28px; height: 20px;
    color: #fff;
  }
  .top-bar .back { position: absolute; left: 15px; top: 4px; }
  .top-bar .title { position: absolute; left: 28px; top: 0; font-size: 12px; line-height: 20px; }
  .top-bar .history { position: absolute; right: 14px; top: 0; font-size: 9px; line-height: 18px; text-decoration: underline; }
  .info-panel {
    position: absolute; left: 0; right: 0; top: 393px; height: 80px;
    background: var(--surface); border-radius: 12px 12px 0 0;
  }
  .info-col { position: absolute; top: 11px; }
  .info-col.time { left: 15px; }
  .info-col.gps { left: 151px; }
  .info-label { font-size: 8.5px; color: var(--link-blue); margin-bottom: 4px; }
  .info-value { font-size: 10.5px; line-height: 15px; color: var(--ink); }
  .camera-bar {
    position: absolute; left: 0; right: 0; top: 460px; bottom: 0;
    background: var(--camera-bar); border-radius: 14px 14px 0 0;
  }
  .camera-bar svg { position: absolute; }

  /* Random check-in screen */
  .text-screen { left: 843px; background: linear-gradient(170deg, var(--surface-soft), #f9f9fa 50%, #ececee); }
  .header-band {
    position: absolute; left: 0; top: 0; width: 100%; height: 80px;
    background: linear-gradient(90deg, var(--brand-blue), var(--brand-blue-light));
    border-radius: 0 0 14px 14px;
    color: #fff;
  }
  .header-band .back { position: absolute; left: 14px; top: 33px; }
  .header-band .title { position: absolute; left: 28px; top: 29px; font-size: 12px; line-height: 20px; font-weight: 600; }
  .avatar {
    position: absolute; left: 197px; top: 28px; width: 22px; height: 22px; border-radius: 50%;
    background: linear-gradient(180deg, #b9b3aa, #6e6357); border: 1.5px solid #fff;
  }
  .header-band .bell { position: absolute; left: 226px; top: 32px; }
  .section-label { position: absolute; left: 14px; top: 109px; font-size: 10.5px; color: var(--ink); }
  .text-input {
    position: absolute; left: 15px; top: 143px; width: 224px; height: 90px;
    border: 1px solid #d8d8da; border-radius: 5px; background: rgba(255,255,255,0.4);
    font-size: 9px; color: var(--ink-soft); padding: 12px 15px;
  }
  .submit-button { top: 253px; height: 25px; line-height: 25px; font-size: 9.5px; width: 224px; }
  .history-link {
    position: absolute; left: 0; right: 0; top: 291px; text-align: center;
    font-size: 9.5px; color: var(--link-blue); text-decoration: underline;
  }
</style>
</head>
<body>

<section class="screen register-screen">
  <h1 class="app-title">Zarvo</h1>
  <div class="register-card">
    <h2 class="card-heading">Register</h2>
    <div class="field" style="top:61px">User Name</div>
    <div class="field" style="top:105px">Email Address</div>
    <div class="field" style="top:149px">Phone Number</div>
    <div class="field" style="top:193px">Date of Birth</div>
    <div class="field" style="top:237px">Password
      <svg class="eye" width="13" height="10" viewBox="0 0 13 10"><path d="M1 5 Q6.5 -1 12 5 Q6.5 11 1 5Z" fill="none" stroke="#9a9a9a" stroke-width="1"/><circle cx="6.5" cy="5" r="1.8" fill="none" stroke="#9a9a9a" stroke-width="1"/></svg>
    </div>
    <div class="primary-button register-button">Let’s Get Started</div>
    <div class="divider"></div>
    <p class="legal">By creating an account, you agree to our<br><b>Terms &amp; Conditions</b> and agree to <b>Privacy Policy</b></p>
  </div>
</section>

<section class="screen camera-screen">
  <div class="photo-area" role="img" aria-label="Live selfie camera view of the client outdoors among autumn trees"></div>
  <div class="top-bar">
    <svg class="back" width="7" height="12" viewBox="0 0 7 12"><path d="M6 1 L1 6 L6 11" fill="none" stroke="#fff" stroke-width="1.6"/></svg>
    <span class="title">Check-in</span>
    <span class="history">View History</span>
  </div>
  <div class="info-panel">
    <div class="info-col time">
      <div class="info-label">Checkin Date &amp; Time</div>
      <div class="info-value">25/11/2022<br>13:00 Pm</div>
    </div>
    <div class="info-col gps">
      <div class="info-label">GPS Location</div>
      <div class="info-value">Long: 47.2549861<br>Lat: 35.2596542</div>
    </div>
  </div>
  <div class="camera-bar">
    <svg style="left:14px;top:35px" width="30" height="18" viewBox="0 0 30 18"><rect x="0" y="0" width="20" height="18" rx="3" fill="#fff"/><path d="M22 6 L30 1 L30 17 L22 12Z" fill="#fff"/></svg>
    <svg style="left:107px;top:24px" width="40" height="40" viewBox="0 0 40 40"><circle cx="20" cy="20" r="18.5" fill="none" stroke="#fff" stroke-width="1.6"/><circle cx="20" cy="20" r="16" fill="var(--shutter)"/></svg>
    <svg style="left:216px;top:33px" width="23" height="23" viewBox="0 0 24 24"><path d="M20 9 A8.5 8.5 0 0 0 4.5 8" fill="none" stroke="#fff" stroke-width="2"/><path d="M20.5 4 L20.5 9.5 L15 9.5" fill="none" stroke="#fff" stroke-width="2"/><path d="M4 15 A8.5 8.5 0 0 0 19.5 16" fill="none" stroke="#fff" stroke-width="2"/><path d="M3.5 20 L3.5 14.5 L9 14.5" fill="none" stroke="#fff" stroke-width="2"/></svg>
  </div>
</section>

<section class="screen text-screen">
  <header class="header-band">
    <svg class="back" width="7" height="12" viewBox="0 0 7 12"><path d="M6 1 L1 6 L6 11" fill="none" stroke="#fff" stroke-width="1.6"/></svg>
    <span class="title">Random Check-in</span>
    <div class="avatar" role="img" aria-label="Client profile photo"></div>
    <svg class="bell" width="12" height="13" viewBox="0 0 12 13"><path d="M2 10 L2 6 A4 4 0 0 1 10 6 L10 10 L11 11 L1 11Z" fill="none" stroke="#fff" stroke-width="1.2"/><path d="M4.5 12 A1.5 1.5 0 0 0 7.5 12" fill="none" stroke="#fff" stroke-width="1.2"/></svg>
  </header>
  <p class="section-label">Check-in via text</p>
  <div class="text-input">Type here...</div>
  <div class="primary-button submit-button">Submit</div>
  <p class="history-link">View History</p>
</section>

</body>
</html>
```